Walk Through Fire Step out, step up and into your best performance

BRIEF FOR BOOK FRONT COVER

• It needs to be iconic
• It needs to be a ‘clean’ design
• Needs to be seen on a bookshelf in an airport from 50 feet away
• No stick like figures/cartoon style or cutesy design
• The book appeals to both male and female readers
• This is a cross over book and covers a couple of genres like Martin Kessler’s book Small Steady Gains or Tessa Holm’s Quiet Mastery. So it is primarily about taking better care of yourself personally, professionally and will appeal to those in business.
• The idea that a personal enriching life feeds into an engaged performer on the job – they feed off each other leading to increased engagement, productivity and fulfillment
• The dance analogy means that you are not sitting on the sidelines of your life or business
• It is laced with inspiring real life case studies
• Positioning of the book: People facing adversity and still come through better than ever and better equipped to what comes next.
• Want a cover that would attract a Pinnacle 40 CEO to buy the book for his staff
• My name as the author should be across the bottom MIRIAM FOSTER MBA MCC
Updates

Project Deadline Extended Reason: A big thank you for all the designers who submitted a cover design and I have been spoilt for choiceI need to finalize the copy on the book cover and hence the need for an extension of time.Thanks for your understanding.Miriam Added Sunday, September 18, 2016

Target Market(s)

Professionals in the age group 25 - 55

Industry/Entity Type

Airport

Contact Information for Business Card

basic information and a very clean look

Logo Text

probably book title more important that it can be seen clearly when the size is reduced to a small size e.g. if sponsoring an event

Number of Pages Required

5+ page

Font styles to use
Sans Serif

Colors
ec1f27
f37122
abd037

Requirements
Must have
• info already provided

```html
<!DOCTYPE html>
<html lang="en">
<head>
<meta charset="utf-8">
<title>Walk Through Fire — Book Cover</title>
<link href="https://fonts.googleapis.com/css2?family=Bebas+Neue&family=Oswald:wght@600&family=Cinzel:wght@400&display=swap" rel="stylesheet">
<style>
  :root {
    --page-bg: #ffffff;
    --cover-coral: #f26b5b;
    --title-cream: #fdf1c6;
    --band-charcoal: #4a4a4a;
    --subtitle-orange: #f5896a;
    --author-ink: #3d3a39;
    --figure-teal: #9dd6d3;
    --figure-dark: #4b4b4b;
  }
  html, body {
    margin: 0;
    padding: 0;
    width: 1200px;
    height: 1000px;
    overflow: hidden;
    background: var(--page-bg);
  }
  .canvas {
    position: relative;
    width: 1200px;
    height: 1000px;
  }
  .book-cover {
    position: absolute;
    left: 320px;
    top: 60px;
    width: 560px;
    height: 880px;
    background: var(--cover-coral);
    overflow: hidden;
  }
  .cover-hero {
    position: absolute;
    left: 400px;
    top: 40px;
    width: 140px;
    height: 520px;
    background: linear-gradient(180deg, var(--figure-teal) 0%, var(--figure-teal) 14%, var(--figure-dark) 30%, var(--figure-dark) 100%);
    border-radius: 6px;
  }
  .cover-title {
    position: absolute;
    left: 40px;
    top: 262px;
    margin: 0;
    font-family: "Bebas Neue", "Oswald", sans-serif;
    font-weight: 400;
    font-size: 110px;
    line-height: 0.92;
    letter-spacing: 2px;
    color: var(--title-cream);
    text-transform: uppercase;
  }
  .cover-title span { display: block; }
  .cover-band {
    position: absolute;
    left: 0;
    top: 540px;
    width: 560px;
    height: 190px;
  }
  .cover-subtitle {
    position: absolute;
    left: 0;
    top: 656px;
    width: 560px;
    margin: 0;
    text-align: center;
    font-family: "Oswald", sans-serif;
    font-weight: 600;
    font-size: 18px;
    line-height: 1.35;
    letter-spacing: 0.5px;
    color: var(--subtitle-orange);
    text-transform: uppercase;
  }
  .cover-author {
    position: absolute;
    left: 0;
    top: 792px;
    width: 560px;
    margin: 0;
    text-align: center;
    font-family: "Cinzel", serif;
    font-size: 22px;
    letter-spacing: 1px;
    word-spacing: 4px;
    color: var(--author-ink);
  }
  .cover-author .credentials { margin-left: 14px; }
</style>
</head>
<body>
<div class="canvas">
  <section class="book-cover">
    <div class="cover-hero" role="img" aria-label="Silhouette of a person leaping joyfully, holding an open umbrella aloft in the rain"></div>

    <h1 class="cover-title">
      <span>Walk</span>
      <span>Through</span>
      <span>Fire</span>
    </h1>

    <svg class="cover-band" viewBox="0 0 560 190" aria-hidden="true">
      <polygon points="0,92 560,6 560,190 0,190" fill="var(--band-charcoal)"/>
    </svg>

    <p class="cover-subtitle">Step out, step up and step into<br>your best performance in business and life</p>

    <p class="cover-author">MIRIAM FOSTER<span class="credentials">MBA MCC</span></p>
  </section>
</div>
</body>
</html>
```